App Company Business Card Design Project

We are looking for a two sided business card design with one side in English and one side in Chinese. Information should include:
1. Name
2. Email
3. Cell phone
4. Address
Please incorporate the logo attached. Above are the only requirements.

Industry/Entity Type

Business

```html
<!DOCTYPE html>
<html lang="en">
<head>
<meta charset="utf-8">
<title>Kestrel Harbor – Business Card</title>
<link rel="stylesheet" href="https://fonts.googleapis.com/css2?family=Noto+Sans+SC:wght@500;700&family=Open+Sans:wght@400;600;700&display=swap">
<style>
  :root {
    --page-bg: #3a3a3a;
    --card-dark: #1b1b1b;
    --card-light: #f4f4f4;
    --ink: #4a4a4a;
    --ink-strong: #2b2b2b;
    --accent: #1fb6d0;
    --rule: #6b6b6b;
    --map-dark: #2a2a2a;
    --map-light: #e6e6e6;
  }
  * { margin: 0; padding: 0; box-sizing: border-box; }
  html, body {
    width: 1200px; height: 964px; overflow: hidden;
    background: var(--page-bg);
    font-family: "Open Sans", Arial, sans-serif;
  }
  .stage {
    position: relative; width: 1200px; height: 964px;
    display: flex; flex-direction: column; align-items: center; justify-content: center; gap: 40px;
  }
  .card {
    position: relative; width: 760px; height: 434px; overflow: hidden;
    box-shadow: 0 10px 30px rgba(0,0,0,.45);
  }
  .world-map {
    position: absolute; inset: 40px 60px;
    border-radius: 40%;
  }

  /* Back side (Chinese) */
  .card--back { background: var(--card-dark); }
  .card--back .world-map {
    background: radial-gradient(ellipse at center, var(--map-dark) 0%, rgba(42,42,42,0) 70%);
  }
  .brand-back {
    position: absolute; left: 0; right: 0; top: 50%; transform: translateY(-50%);
    display: flex; align-items: center; justify-content: center; gap: 22px;
  }
  .brand-back .brand-dot { width: 54px; height: 54px; border-radius: 50%; background: var(--accent); flex: none; }
  .brand-back .brand-name {
    color: #ffffff; font-family: "Noto Sans SC", "Open Sans", sans-serif;
    font-weight: 500; font-size: 52px; letter-spacing: 6px; line-height: 1;
  }

  /* Front side (English) */
  .card--front { background: var(--card-light); }
  .card--front .world-map {
    background: radial-gradient(ellipse at center, var(--map-light) 0%, rgba(230,230,230,0) 70%);
  }
  .brand-front {
    position: absolute; left: 48px; top: 175px;
    display: flex; align-items: center; gap: 14px;
  }
  .brand-front .brand-dot { width: 34px; height: 34px; border-radius: 50%; background: var(--accent); flex: none; }
  .brand-front .brand-name {
    color: var(--ink); font-weight: 600; font-size: 34px; letter-spacing: .5px; white-space: nowrap;
  }
  .divider {
    position: absolute; left: 430px; top: 86px; width: 1px; height: 176px; background: var(--rule);
  }
  .contact { position: absolute; left: 458px; top: 82px; color: var(--ink); }
  .person-name { font-weight: 700; font-size: 22px; color: var(--ink-strong); letter-spacing: .5px; }
  .person-name .surname { color: var(--accent); }
  .person-role { font-size: 15px; letter-spacing: 1px; margin-top: 2px; }
  .contact-row { display: flex; align-items: center; gap: 12px; margin-top: 20px; font-size: 14px; line-height: 1.3; }
  .contact-icon {
    width: 32px; height: 32px; border-radius: 50%; background: var(--accent);
    display: flex; align-items: center; justify-content: center; flex: none;
  }
  .address {
    position: absolute; left: 0; right: 0; bottom: 44px; text-align: center;
    font-size: 15px; color: var(--ink-strong);
  }
</style>
</head>
<body>
<main class="stage">
  <section class="card card--back" lang="zh-Hans" aria-label="Card back, Chinese side">
    <div class="world-map" role="img" aria-label="Faint world map in the background"></div>
    <div class="brand-back">
      <span class="brand-dot"></span>
      <span class="brand-name">茶隼港创投</span>
    </div>
  </section>

  <section class="card card--front" aria-label="Card front, English side">
    <div class="world-map" role="img" aria-label="Faint world map in the background"></div>
    <div class="brand-front">
      <span class="brand-dot"></span>
      <span class="brand-name">KESTREL HARBOR</span>
    </div>
    <div class="divider"></div>
    <div class="contact">
      <p class="person-name">ALEX <span class="surname">MORGAN</span></p>
      <p class="person-role">GENERAL MANAGER</p>
      <div class="contact-row">
        <span class="contact-icon">
          <svg width="16" height="16" viewBox="0 0 24 24" aria-hidden="true"><path fill="#fff" d="M6.6 10.8a15.1 15.1 0 0 0 6.6 6.6l2.2-2.2c.3-.3.7-.4 1-.2 1.1.4 2.3.6 3.6.6.6 0 1 .4 1 1V20c0 .6-.4 1-1 1A17 17 0 0 1 3 4c0-.6.4-1 1-1h3.5c.6 0 1 .4 1 1 0 1.3.2 2.5.6 3.6.1.3 0 .7-.2 1z"/></svg>
        </span>
        <div><p>010 482 7315</p><p>138 2604 9147</p></div>
      </div>
      <div class="contact-row">
        <span class="contact-icon">
          <svg width="18" height="18" viewBox="0 0 24 24" aria-hidden="true"><rect x="3" y="4" width="18" height="12" rx="1" fill="none" stroke="#fff" stroke-width="2"/><path d="M9 20h6M12 16v4" stroke="#fff" stroke-width="2"/></svg>
        </span>
        <div><p>alex@kestrelharbor.com</p><p>www.kestrelharbor.com</p></div>
      </div>
    </div>
    <p class="address">42, Linden Park Road, 5th Floor, Tower B</p>
  </section>
</main>
</body>
</html>
```